Clean book cover design for book about writing a book

Book title: The Crossing
Subtitle: 9 Paths to Crafting a Volume that Counts
Name: Marisol T. Brenwick, The Quill Nursery

This is a book which teaches 10 steps to writing a self-help book. I'm looking for a very clean impactful cover either with no image or just a small simple image of a book, typewriter, laptop, cabin or something very simple. I am attaching the manuscript here if reading it would help you with the cover. The theme of the book is that you can write with joy and ease and your book can just flow out of you if you learn how to clear the blocks between you and your book already written. Sort of a new agey stance on book writing.

The book should generally match the branding on my website. Www.TheQuillNursery.example.

I have photos of myself attached which I'd like used for the back cover with an "about the author section of maybe 50 words.

The project is for the full back cover and spine as well as the front cover (see print Forge template attached) but to win the contest you can just design the front cover and then I'll give the winner the template for the full design with the back cover copy. Or you can design the full cover using the template and you can use Loren ipsum text if you need to.

My clients are very upmarket and the themes of my business revolve around nuturing and incubating ideas and authors. Very feminine creation energy.

For colors see The Crossing Press (CB) wax seals and the background fades. I don't want my logo on the cover but I am attaching it here so you get a feel for the branding. The logo is in the LOBSTER font and you can see how we do the grey with the rainbow shadow.

Here are some covers I like:

http://www.shopvale.example/Pen-Tome-Quick-Stage---Stage/dp/055817342Q
http://www.shopvale.example/Plotting-Your-Tale-Chart-Triumph/dp/0841739265
http://www.shopvale.example/Be-Scribe-Seeking-Voice-Guide-ebook/dp/K22R9WQ3L1
http://www.shopvale.example/Strays-Tale-Triumph-Rupert-Vanhollow/dp/0552048871
Updates

I have revised my brief to include some picture and images that will help you create the cover. I have also included some of my favorite covers to give you more of a sense of what I'm going for. And I have included the manuscript in case it would help you to skim through it in order to get a sense of the reader and the book. I think if you look at my revised brief it will make it easier to create a submission. Thanks!

Target Market(s)

Women 40-60 who run small businesses as life coaches or other healing jobs (therapy, reiki, light work) they have a spiritual/new age bent.

Industry/Entity Type

Business

Font styles to use
Serif
Other font styles liked:
• Lobster (not required... just a suggestion since it's my logo font)

Requirements
Must have
• Name and title easy to read in 1" x 1" thumb nail
Nice to have
• Fantastic type face treatment.

Match the look and feel of my website.
Should not have
• Busy images. With one simple image or just designed with colors and typeface treatment

```html
<!DOCTYPE html>
<html lang="en">
<head>
<meta charset="utf-8">
<title>The Crossing — Book Cover</title>
<link rel="stylesheet" href="https://fonts.googleapis.com/css2?family=Oswald:wght@300;400&family=Oranienbaum&display=swap">
<style>
  :root {
    --backdrop: #e9e9ea;
    --paper: #ffffff;
    --ink: #1f1f1f;
    --ink-soft: #3a3a3a;
    --blue: #4aa9dc;
    --yellow: #f3cc1e;
    --pink: #ec4f9f;
    --orange: #f58a48;
    --cyan: #6bcbe0;
    --green: #b4d44c;
    --seal: #2f9fb0;
  }
  * { margin: 0; padding: 0; box-sizing: border-box; }
  html, body {
    width: 1200px; height: 1116px; overflow: hidden;
    background: var(--backdrop);
  }
  .cover {
    position: absolute; left: 168px; top: 0;
    width: 864px; height: 1116px;
    background: var(--paper);
    overflow: hidden;
  }
  .title-the {
    position: absolute; left: 56px; top: 100px;
    writing-mode: vertical-rl; transform: rotate(180deg);
    font-family: "Oranienbaum", serif;
    font-size: 58px; line-height: 1; letter-spacing: 2px;
    color: var(--blue);
  }
  .title-main {
    position: absolute; left: 124px; top: 78px;
    font-family: "Oswald", sans-serif; font-weight: 400;
    font-size: 178px; line-height: 1; letter-spacing: 4px;
    white-space: nowrap;
  }
  .c-yellow { color: var(--yellow); }
  .c-pink { color: var(--pink); }
  .c-orange { color: var(--orange); }
  .c-cyan { color: var(--cyan); }
  .c-green { color: var(--green); }

  .idea-art {
    position: absolute; left: 360px; top: 293px;
    width: 425px; height: 294px;
    background: radial-gradient(ellipse at 55% 45%, #f7d23a 0%, #f9e58a 35%, #ffffff 72%);
  }
  .pen-art {
    position: absolute; left: 497px; top: 700px;
    width: 367px; height: 168px;
    background: linear-gradient(160deg, #ffffff 10%, #5d6161 55%, #c9a24a 72%, #ffffff 95%);
    opacity: .85;
  }

  .subtitle {
    position: absolute; left: 52px; top: 486px;
    font-family: "Oranienbaum", serif; color: var(--ink);
    line-height: 1; white-space: nowrap;
  }
  .subtitle .line { display: block; }
  .sub-count { font-size: 104px; }
  .sub-paths { font-size: 50px; letter-spacing: 28px; margin-left: 10px; }
  .sub-to { font-size: 84px; letter-spacing: -3px; margin-top: 14px; }
  .sub-volume { font-size: 82px; letter-spacing: 3px; margin-top: 14px; }
  .sub-counts { font-size: 60px; letter-spacing: -1px; margin-top: 22px; }

  .author {
    position: absolute; left: 63px; top: 1000px;
    font-family: "Oswald", sans-serif; font-weight: 300;
    font-size: 21px; line-height: 34px; letter-spacing: 1px;
    color: var(--ink-soft); text-transform: uppercase;
  }
  .publisher {
    position: absolute; right: 68px; top: 1000px;
    display: flex; align-items: center; gap: 10px;
  }
  .publisher-dot {
    width: 56px; height: 56px; border-radius: 50%;
    background: var(--seal);
  }
  .publisher-name {
    font-family: "Oswald", sans-serif; font-weight: 400;
    font-size: 22px; color: var(--seal);
  }
</style>
</head>
<body>
  <main class="cover">
    <h1>
      <span class="title-the">THE</span>
      <span class="title-main"><span class="c-yellow">CR</span><span class="c-pink">OS</span><span class="c-orange">SI</span><span class="c-cyan">N</span><span class="c-green">G</span></span>
    </h1>

    <div class="idea-art" role="img" aria-label="Crumpled yellow paper lightbulb with colourful sketched arrows"></div>

    <h2 class="subtitle">
      <span class="line"><span class="sub-count">9</span><span class="sub-paths">PATHS</span></span>
      <span class="line sub-to">TO CRAFTING</span>
      <span class="line sub-volume">A VOLUME</span>
      <span class="line sub-counts">THAT COUNTS</span>
    </h2>

    <div class="pen-art" role="img" aria-label="Black and gold fountain pen resting on the page"></div>

    <p class="author">Marisol T. Brenwick,<br>The Quill Nursery</p>

    <div class="publisher">
      <span class="publisher-name">CB</span>
      <span class="publisher-dot"></span>
    </div>
  </main>
</body>
</html>
```